Corvane Holdings , new business card design

investment firm with corporate clients . need double sided business card , vertical and horizontal options ,logo must be clear. prefer pantone colors only and sharp design. website also www.corvane-example.ae

Khalid Bin Rashed
Managing Director
Tel. +971 4 000 3829
Mobile +971 50 000 4172
khalid@corvane-example.ae
Palm Crest Tower, officw 18-B07, Qasr Gardens, Dubai

Contact Information for Business Card

Khalid Bin Rashed
Managing Director

Font styles to use
Serif

Colors

Designer to choose colors to be used in the design.

```html
<!DOCTYPE html>
<html lang="en">
<head>
<meta charset="utf-8">
<title>Corvane Holdings – Business Card</title>
<link rel="stylesheet" href="https://fonts.googleapis.com/css2?family=Lato:wght@300;400&display=swap">
<style>
  :root {
    --page-bg: #e8e8e6;
    --card-white: #f7f7f6;
    --brand-blue: #426d95;
    --ink: #2a2a2a;
    --ink-soft: #3a3a3a;
    --rule: #555555;
    --on-blue: #ffffff;
  }
  * { margin: 0; padding: 0; box-sizing: border-box; }
  html, body {
    width: 1200px; height: 1200px; overflow: hidden;
    background: var(--page-bg);
    font-family: "Lato", Arial, sans-serif;
    color: var(--ink);
  }
  .canvas { position: relative; width: 1200px; height: 1200px; }

  .card {
    position: absolute; left: 150px;
    width: 900px; height: 514px;
    background: var(--card-white);
    box-shadow: 0 6px 18px rgba(0,0,0,0.12);
    overflow: hidden;
  }
  .card--front { top: 60px; }
  .card--back  { top: 626px; }

  /* Front side */
  .front-brand {
    position: absolute; left: 0; right: 0; top: 50%;
    transform: translateY(-50%);
    display: flex; align-items: center; justify-content: center; gap: 22px;
  }
  .front-brand__mark {
    width: 22px; height: 22px; background: var(--brand-blue);
  }
  .front-brand__name {
    font-weight: 300; font-size: 40px; letter-spacing: 12px;
    color: var(--ink); text-transform: uppercase;
  }

  /* Back side */
  .back-curve { position: absolute; inset: 0; }
  .contact { position: absolute; left: 70px; top: 62px; width: 580px; }
  .contact__name { font-size: 40px; font-weight: 400; line-height: 1.1; }
  .contact__title { font-size: 22px; font-weight: 400; color: var(--ink-soft); margin-top: 4px; }
  .contact__rule { height: 2px; background: var(--rule); margin: 22px 0 20px; }
  .contact__rule--short { width: 480px; }
  .contact__list { display: grid; grid-template-columns: 110px 20px auto; row-gap: 6px; font-size: 29px; }
  .contact__label, .contact__colon, .contact__value { line-height: 1.2; }
  .contact__address { font-size: 21px; line-height: 1.35; color: var(--ink-soft); }

  .back-brand {
    position: absolute; right: 46px; top: 64px;
    writing-mode: vertical-rl;
    font-weight: 300; font-size: 26px; letter-spacing: 7px;
    color: var(--on-blue); text-transform: uppercase;
  }
  .back-web {
    position: absolute; right: 116px; top: 150px;
    writing-mode: vertical-rl;
    font-size: 22px; font-weight: 400; color: var(--on-blue);
  }
</style>
</head>
<body>
<main class="canvas">

  <section class="card card--front" aria-label="Card front">
    <div class="front-brand">
      <span class="front-brand__mark"></span>
      <span class="front-brand__name">Corvane Holdings</span>
    </div>
  </section>

  <section class="card card--back" aria-label="Card back">
    <svg class="back-curve" width="900" height="514" viewBox="0 0 900 514" aria-hidden="true">
      <path d="M310 514 Q640 480 740 0 L900 0 L900 514 Z" fill="var(--brand-blue)"/>
    </svg>

    <div class="contact">
      <h1 class="contact__name">Khalid Bin Rashed</h1>
      <p class="contact__title">Managing Director</p>
      <div class="contact__rule"></div>
      <div class="contact__list">
        <span class="contact__label">Tel</span><span class="contact__colon">:</span><span class="contact__value">+971 4 000 3829</span>
        <span class="contact__label">Mobile</span><span class="contact__colon"></span><span class="contact__value">+971 50 000 4172</span>
        <span class="contact__label">Email</span><span class="contact__colon">:</span><span class="contact__value">khalid@corvane-example.ae</span>
      </div>
      <div class="contact__rule contact__rule--short"></div>
      <p class="contact__address">Palm Crest Tower, officw 18-B07,<br>Qasr Gardens, Dubai</p>
    </div>

    <div class="back-brand">Corvane Holdings</div>
    <div class="back-web">www.corvane-example.ae</div>
  </section>

</main>
</body>
</html>
```